Brand refresh of quote, work docket and Fire certificate documents

I would like a refresh of our document suit including

1. Front page called VOLT3 Proposal
2. Quote document template
3. Work docket template
4. Fire certificate template - to look like a professional complaint certificate

Examples of documents are attached.

```html
<!DOCTYPE html>
<html lang="en">
<head>
<meta charset="utf-8">
<title>VOLT3 Proposal – Cover</title>
<link href="https://fonts.googleapis.com/css2?family=Open+Sans:wght@300;400;600;700;800&display=swap" rel="stylesheet">
<style>
  :root{
    --backdrop:#d5d8d7;
    --paper:#ffffff;
    --brand-red:#c8202f;
    --ink:#383838;
    --ink-soft:#4a4a4a;
    --faint:#e4e4e4;
    --faint-line:#d6d6d6;
    --sky-top:#3a4d9a;
    --sky-mid:#5a6fb4;
    --city-low:#4a3f4c;
  }
  *{margin:0;padding:0;box-sizing:border-box}
  html,body{width:1200px;height:1200px;overflow:hidden;background:var(--backdrop);font-family:"Open Sans",sans-serif;color:var(--ink)}
  .cover{position:absolute;left:271px;top:134px;width:658px;height:931px;background:var(--paper);overflow:hidden}
  .divider{position:absolute;left:477px;top:0;width:1.5px;height:163px;background:var(--brand-red)}
  .brand{position:absolute;left:45px;top:60px}
  .brand-name{font-size:80px;font-weight:800;line-height:1;color:var(--ink);letter-spacing:-1px}
  .brand-tag{position:absolute;left:45px;top:151px;font-size:10px;font-weight:400;letter-spacing:5.6px;color:var(--ink-soft);white-space:nowrap}
  .company{position:absolute;left:491px;top:83px;font-size:10.8px;line-height:15px;color:var(--ink-soft)}
  .company .name{color:var(--brand-red);font-weight:700;font-size:11.5px}
  .company .gap{margin-top:3px}
  .company b{font-weight:700;color:var(--ink)}
  .company .mail{display:flex;align-items:center;gap:5px;margin-top:3px}
  .title{position:absolute;left:45px;top:208px;font-weight:700;line-height:1}
  .title .line-brand{display:block;font-size:70px;color:var(--brand-red)}
  .title .line-doc{display:block;font-size:74px;color:var(--ink);margin-top:-2px;letter-spacing:-0.5px}
  .title-rule{position:absolute;left:47px;top:350px;width:330px;height:2px;background:var(--brand-red)}
  .meta{position:absolute;left:47px}
  .meta .icon{position:absolute;left:0}
  .meta .label{color:var(--brand-red);font-weight:600;font-size:15.5px;line-height:21.5px}
  .meta .value{font-size:16px;line-height:21.7px}
  .meta strong{font-weight:600}
  .date{top:379px}
  .date .value{padding-left:26px;font-weight:600;font-size:16px}
  .client{top:421px}
  .location{top:552px}
  .location .text,.proposal .text{padding-left:26px}
  .proposal{top:617px}
  .cityscape{position:absolute;left:0;top:675px;width:382px;height:210px;background:linear-gradient(180deg,var(--sky-top) 0%,var(--sky-mid) 40%,#7c7f9e 65%,var(--city-low) 100%)}
  .footer{position:absolute;left:0;top:884px;width:658px;height:47px;background:var(--brand-red);color:#fff;font-weight:700;font-size:17.5px;display:flex;align-items:center;justify-content:center}
  .side-mark{position:absolute;left:460px;top:290px}
</style>
</head>
<body>
<main class="cover">
  <div class="divider"></div>

  <div class="brand"><div class="brand-name">VOLT3</div></div>
  <div class="brand-tag">PASSIVE FIRE PROTECTION</div>

  <address class="company" style="font-style:normal">
    <div class="name">VOLT3 Pty Ltd</div>
    <div>4/22 Larkfield Road</div>
    <div>Bayswater VIC 3153</div>
    <div class="gap"><b>ABN:</b> 48 203 615 907</div>
    <div class="mail">
      <svg width="13" height="10" viewBox="0 0 13 10"><rect x="0.5" y="0.5" width="12" height="9" fill="var(--brand-red)"/><path d="M0.5 0.5 L6.5 5.5 L12.5 0.5" fill="none" stroke="#fff" stroke-width="1"/></svg>
      <span>admin@volt3.com.au</span>
    </div>
  </address>

  <h1 class="title"><span class="line-brand">VOLT3</span><span class="line-doc">PROPOSAL</span></h1>
  <div class="title-rule"></div>

  <div class="meta date">
    <svg class="icon" width="16" height="16" viewBox="0 0 16 16" style="top:3px"><rect x="1" y="2.5" width="14" height="12.5" rx="1.5" fill="none" stroke="var(--brand-red)" stroke-width="1.5"/><rect x="1" y="2.5" width="14" height="3" fill="var(--brand-red)"/><line x1="4.5" y1="0.5" x2="4.5" y2="4" stroke="var(--brand-red)" stroke-width="1.5"/><line x1="11.5" y1="0.5" x2="11.5" y2="4" stroke="var(--brand-red)" stroke-width="1.5"/><g fill="var(--brand-red)"><rect x="3.5" y="7.5" width="2" height="1.5"/><rect x="7" y="7.5" width="2" height="1.5"/><rect x="10.5" y="7.5" width="2" height="1.5"/><rect x="3.5" y="10.8" width="2" height="1.5"/><rect x="7" y="10.8" width="2" height="1.5"/><rect x="10.5" y="10.8" width="2" height="1.5"/></g></svg>
    <div class="value">26th October, 2023</div>
  </div>

  <div class="meta client">
    <div class="label">PREPARED FOR</div>
    <div class="value"><strong>Marlow Constructions</strong></div>
    <div class="value">118 Harbour Rd</div>
    <div class="value">Southbank VIC 3006</div>
    <div class="value">Lorenzo</div>
  </div>

  <div class="meta location">
    <svg class="icon" width="14" height="21" viewBox="0 0 14 21" style="top:10px"><path d="M7 0.5 C3.2 0.5 0.5 3.3 0.5 7 C0.5 11.5 7 20.5 7 20.5 C7 20.5 13.5 11.5 13.5 7 C13.5 3.3 10.8 0.5 7 0.5 Z" fill="var(--brand-red)"/><circle cx="7" cy="7" r="2.6" fill="#fff"/></svg>
    <div class="text">
      <div class="label">PROJECT/WORKS LOCATION</div>
      <div class="value"><strong>47 Ashby Street, Kensington</strong></div>
    </div>
  </div>

  <div class="meta proposal">
    <svg class="icon" width="17" height="17" viewBox="0 0 17 17" style="top:10px"><path d="M2 1 H10 L13 4 V15.5 H2 Z" fill="none" stroke="var(--brand-red)" stroke-width="1.2"/><g stroke="var(--brand-red)" stroke-width="1"><line x1="4" y1="6" x2="10" y2="6"/><line x1="4" y1="8.5" x2="9" y2="8.5"/><line x1="4" y1="11" x2="8" y2="11"/></g><path d="M9.5 13.5 L15.5 6.5 L16.5 7.5 L10.5 14.5 L9 15 Z" fill="var(--brand-red)"/></svg>
    <div class="text">
      <div class="label">PROPOSAL NO</div>
      <div class="value"><strong>1188</strong></div>
    </div>
  </div>

  <div class="cityscape" role="img" aria-label="Photo of a city skyline at dusk with lit high-rise towers and a busy street"></div>

  <svg class="side-mark" width="200" height="565" viewBox="0 0 200 565" aria-hidden="true">
    <text transform="translate(158 560) rotate(-90)" font-family="Open Sans, sans-serif" font-weight="800" font-size="165" fill="var(--faint)" textLength="556" lengthAdjust="spacingAndGlyphs">VOLT3</text>
    <text transform="translate(196 560) rotate(-90)" font-family="Open Sans, sans-serif" font-weight="300" font-size="30" fill="var(--faint-line)" textLength="556" lengthAdjust="spacing">PASSIVE FIRE PROTECTION</text>
  </svg>

  <footer class="footer">www.volt3.com.au</footer>
</main>
</body>
</html>
```